We want to design total new business card and logo for Korvel Building Services Ltd

Our company name Korvel Building Services Ltd. Design new logo and business card , need hi-end luxury style art for architecture and construction industry. The card should simple but stylish. Our business focus on CONNECT tradesman to construction company, help marketing construction company tender oversea projects, managing franchise in construction sector, delivery amazing services to our client, so Logo should show the CONNECTION IDEA, CONNECTING PEOPLE, LUXURY. Visit our website for more information: korvelhub.co.nz

Target Market(s)

Directors or managers

Industry/Entity Type

Construction Company

Contact Information for Business Card

Name, Title, Mobile, Email, Website

Font styles to use
Serif

Colors

Designer to choose colors to be used in the design.

Requirements
Must have
• Simple and luxury, connection icon
Nice to have
• Special materials, plastic card, look through,...
• Look new ideas.

```html
<!DOCTYPE html>
<html lang="en">
<head>
<meta charset="utf-8">
<title>Korvel Building Services Ltd — Business Card</title>
<link rel="stylesheet" href="https://fonts.googleapis.com/css2?family=Tinos:wght@400;700&display=swap">
<style>
  :root {
    --stage: #1b1b1b;
    --stage-light: #2a2a2a;
    --card: #161616;
    --card-edge: #202020;
    --brand-blue: #3a7fd0;
    --sky-blue: #12a8ea;
    --ink-white: #f4f4f4;
    --serif: "Tinos", "Times New Roman", serif;
  }
  * { box-sizing: border-box; margin: 0; padding: 0; }
  html, body { width: 1200px; height: 1200px; overflow: hidden; }
  body {
    background: radial-gradient(ellipse at 70% 30%, var(--stage-light), var(--stage) 70%);
    font-family: var(--serif);
    position: relative;
  }
  .card {
    position: absolute;
    left: 150px;
    width: 900px;
    height: 500px;
    background: linear-gradient(160deg, var(--card-edge), var(--card));
    box-shadow: 0 18px 40px rgba(0,0,0,0.6);
  }
  .card--front { top: 70px; }
  .card--back { top: 630px; }

  .wordmark {
    position: absolute;
    display: flex;
    flex-direction: column;
    align-items: center;
    color: var(--ink-white);
    font-weight: 400;
    text-transform: uppercase;
    text-align: center;
  }
  .wordmark__dot {
    width: 64px; height: 64px;
    border-radius: 50%;
    background: var(--sky-blue);
    margin-bottom: 26px;
  }
  .wordmark__main { font-size: 46px; letter-spacing: 3px; line-height: 1.05; }
  .wordmark__sub { font-size: 26px; letter-spacing: 3px; line-height: 1.3; }

  .card--front .wordmark { left: 330px; top: 120px; width: 420px; }
  .card--back .wordmark { left: 470px; top: 180px; width: 400px; }

  .holder { position: absolute; left: 100px; top: 60px; }
  .holder__name { font-size: 40px; font-weight: 700; color: var(--brand-blue); letter-spacing: 1px; }
  .holder__title { font-size: 20px; color: var(--ink-white); margin-top: 2px; }

  .contacts { position: absolute; left: 100px; bottom: 70px; list-style: none; }
  .contacts__item {
    display: flex; align-items: center; gap: 16px;
    font-size: 22px; color: var(--ink-white);
    margin-top: 8px;
  }
  .contacts__icon { width: 22px; height: 22px; flex: none; }
</style>
</head>
<body>
  <section class="card card--front" aria-label="Card front">
    <div class="wordmark">
      <span class="wordmark__dot"></span>
      <span class="wordmark__main">Korvel Building</span>
      <span class="wordmark__sub">Services Ltd</span>
    </div>
  </section>

  <section class="card card--back" aria-label="Card back">
    <div class="holder">
      <p class="holder__name">Marcus Hale</p>
      <p class="holder__title">Managing Director</p>
    </div>

    <ul class="contacts">
      <li class="contacts__item">
        <svg class="contacts__icon" viewBox="0 0 22 22" fill="none" stroke="#3a7fd0" stroke-width="2">
          <rect x="6" y="1" width="10" height="20" rx="2"/><line x1="9" y1="17" x2="13" y2="17"/>
        </svg>
        214-555-0187
      </li>
      <li class="contacts__item">
        <svg class="contacts__icon" viewBox="0 0 22 22" fill="#3a7fd0">
          <path d="M1 5h20v12H1z"/><path d="M1 5l10 7 10-7" fill="none" stroke="#161616" stroke-width="1.6"/>
        </svg>
        marcushale@korvelhub.co.nz
      </li>
      <li class="contacts__item">
        <svg class="contacts__icon" viewBox="0 0 22 22" fill="none" stroke="#3a7fd0" stroke-width="1.6">
          <circle cx="11" cy="11" r="9.5"/><ellipse cx="11" cy="11" rx="4" ry="9.5"/>
          <line x1="1.5" y1="11" x2="20.5" y2="11"/><line x1="3" y1="6" x2="19" y2="6"/><line x1="3" y1="16" x2="19" y2="16"/>
        </svg>
        www.korvelhub.co.nz
      </li>
    </ul>

    <div class="wordmark">
      <span class="wordmark__dot"></span>
      <span class="wordmark__main">Korvel Building</span>
      <span class="wordmark__sub">Services Ltd</span>
    </div>
  </section>
</body>
</html>
```